Vacation/Holiday Home Wordpress Website

I currently have a website for our vacation/holiday rental home. It is 6 years old and needs a complete redesign to acommodate many new features available today. The existing website can be seen at www.coralwindstays.co.uk . The purpose of the website is mainly to provide useful infomation about our home, the destination of Barbados. The customer is also able to check availability and book. Please note that there is a booking element to the website which is hosted externally. This can be seen at

http://stay.reservequick-hub.net/PickArrival_Mini.asp?ref=kTR%3DWQPA%26LMN%3DHXJX

I now wish to add key functionality such as:

- Video of property and area
- Customer video testimonials
- Other useful information

The navigation, menus and buttons need to be re designed to give a modern, innovative and professional look and feel.

My customers are mainly females between the ages of 35 and 55. The website needs to reassure customers who are parting with a lot of mony by booking online. It needs to give a sense of trust as this may be a once in a lifetime trip which they have saved up for for a long time. Many visitors to the website will be referred by other websites such as www.nestroam.co.uk and www.villaquarters.co.uk.
Updates

Dear designers, 

Thank you for taking the time to write some further comments to you all. 

1. The homepage should have an availability search function as a key feature

2. The look and feel does NOT need to have the 3 feature columns like my current website has

3.  There should not be too much text on the homepage. Brief text can be included with 'more'  buttons to reveal more information 

4.  For designs that are under consideration, we will need to see a design for the other pages as they will be different to the homepage. Information from other pages on the existing website can be used. 

Reason: Dear all, I will be providing extensive feedback later today following a review that we have conducted with a group of our guests. To enable you to read and use this information, we have extended the deadline by 5 days. Thank you for the design submisions so far. We hope that the additional feedback will enable you to amend your designs appropriately. Regards Martin Elswick

Dear all,

Thank you for your designs.  I apologise that I am unable to give detailed feedback on each and every design submitted.  I will contact you individually and indicate whether we would like you to submit any further designs.  These should take into account the feedback below.

Feedback from design review group

1.  Logo should not be displayed in a white box.  It should blend in with the background or be overlayed onto the picture.

2.  There must be an availability calendar on the home page.

3.  Any background image should be subtle, maybe blurred and not distract from the main area.

4.  Text should be limited to a few key words with a 'read more' button to reveal more information.

5.  A gallery/slide show should be featured in the top part of the screen

6.  Icons can be used as navigation buttons

7.  Video testimonials is a key feature and should appear on the home page

8.   The use of bold and vibrant colours is preferred

9.   The 3 column format of the old website should not be copied

Regards

Martin

Target Market(s)

Female's, Families, 35 to 55 year olds, travellers to Barbados

Industry/Entity Type

Online

Requirements
Must have
• Pictures
Video
Testimonials
Clear and stylish navigation
Easy to use navigation
Should not have
• Dated look or feel

```html
<!DOCTYPE html>
<html lang="en">
<head>
<meta charset="utf-8">
<title>Coralwind Stays – Holiday Home in Barbados</title>
<link href="https://fonts.googleapis.com/css2?family=Open+Sans:wght@300;400;600&family=Signika:wght@300;400;600&display=swap" rel="stylesheet">
<style>
:root{
  --blue:#1f5fc8;
  --blue-light:#3f86e4;
  --heading-blue:#1d5cb6;
  --red:#e2302a;
  --orange:#ee5424;
  --yellow:#ffb400;
  --text:#333;
  --muted:#7a7a7a;
  --line:#e2e2e2;
  --footer:#f3f3f3;
}
*{box-sizing:border-box;margin:0;padding:0}
html,body{width:893px;height:1200px;overflow:hidden;background:#fff}
body{font-family:"Open Sans",sans-serif;color:var(--text);position:relative}
.abs{position:absolute}
.page{position:relative;width:893px;height:1200px;overflow:hidden}

/* header */
.masthead{position:absolute;left:0;top:0;width:893px;height:440px;
  background:linear-gradient(180deg,#2a78d2 0%,#6fb0ea 22%,#b9daf2 45%,#d4e6f0 70%,#ece6dc 100%)}
.brand{left:60px;top:52px;display:flex;align-items:center;gap:8px;
  font-family:"Signika",sans-serif;font-weight:400;font-size:22px;letter-spacing:3px;color:var(--red);text-transform:uppercase}
.brand-dot{width:14px;height:14px;border-radius:50%;background:var(--red)}
.search{left:645px;top:63px;width:198px;height:26px;background:#fff;border-radius:4px;
  display:flex;align-items:center;justify-content:space-between;padding:0 8px;font-size:10px;font-style:italic;color:#999}

.nav{left:49px;top:101px;width:797px;height:41px;display:flex;
  background:linear-gradient(180deg,var(--blue-light),var(--blue));border-radius:3px 3px 0 0}
.nav a{color:#fff;text-decoration:none;font-family:"Signika",sans-serif;font-weight:600;font-size:14px;
  display:flex;align-items:center;padding:0 17px;border-right:1px solid rgba(255,255,255,.35)}
.nav a:last-child{border-right:0}

.hero{left:49px;top:142px;width:797px;height:271px;overflow:hidden;border-radius:0 0 3px 3px}
.hero-photo{position:absolute;left:0;top:0;width:580px;height:271px;
  background:linear-gradient(160deg,#14386a 0%,#3d6ea3 35%,#c9b8a0 60%,#6b4b30 85%,#2a2a2e 100%)}
.hero-panel{position:absolute;left:520px;top:0;width:277px;height:271px;background:var(--yellow);
  clip-path:polygon(44px 0,100% 0,100% 100%,0 100%)}
.hero-copy{left:634px;top:178px;width:200px;color:#fff}
.hero-copy h1{font-family:"Signika",sans-serif;font-weight:600;font-size:22px;line-height:1.2}
.hero-copy p{font-size:10px;line-height:15px;margin-top:8px;font-weight:300}
.dots{display:flex;gap:4px;margin-top:9px}
.dots span{width:9px;height:9px;border-radius:50%;background:#fff}

/* content */
.welcome{left:49px;top:470px;width:550px}
.welcome h2{font-family:"Signika",sans-serif;font-weight:300;font-size:21px;color:var(--red)}
.welcome h2 b{font-weight:400}
.welcome .lead{font-size:12px;margin-top:8px;color:#333}
.welcome p.body{font-size:10px;line-height:19px;color:var(--muted);margin-top:6px}

.section-title{font-family:"Signika",sans-serif;font-weight:300;font-size:18px;color:#333}
.properties{left:49px;top:605px}
.prop{position:absolute;top:33px;width:173px}
.thumb{width:173px;height:98px;border-radius:3px;position:relative}
.play{position:absolute;left:50%;top:50%;width:30px;height:30px;margin:-15px;border-radius:50%;
  background:#1c1c1c;border:2px solid #fff;display:flex;align-items:center;justify-content:center}
.prop h3{font-family:"Signika",sans-serif;font-weight:400;font-size:14px;margin-top:8px}
.prop p{font-size:10px;color:var(--muted);margin-top:2px}

.features{left:49px;top:820px}
.features h2,.attractions h2{font-family:"Signika",sans-serif;font-weight:300;font-size:18px;color:var(--orange)}
.features ul{list-style:none;margin-top:12px}
.features li{font-size:10.5px;color:var(--orange);height:23.2px;display:flex;align-items:center;gap:6px}

.attractions{left:316px;top:820px;width:270px}
.attractions p{font-size:10px;line-height:15.5px;color:var(--muted);margin-top:10px}
.attr-list{position:absolute;top:92px;list-style:none;font-size:10px;color:#444}
.attr-list li{height:23.2px;display:flex;align-items:center;gap:6px}
.attr-list li::before{content:"";border-left:5px solid #333;border-top:4px solid transparent;border-bottom:4px solid transparent}

/* sidebar */
.calendar-block{left:632px;top:472px;width:205px}
.sidebar-title{font-family:"Signika",sans-serif;font-weight:400;font-size:18px;color:var(--heading-blue)}
.calendar{margin-top:8px;width:205px;border:1px solid var(--line);border-radius:3px;overflow:hidden}
.cal-head{height:27px;background:linear-gradient(180deg,var(--blue-light),var(--blue));color:#fff;
  display:flex;align-items:center;justify-content:space-between;padding:0 10px;font-family:"Signika",sans-serif;font-size:13px}
.cal-days,.cal-row{display:grid;grid-template-columns:repeat(7,1fr)}
.cal-days{background:var(--orange);color:#fff;font-size:10px;height:21px;align-items:center;text-align:center}
.cal-row{height:23.5px;border-top:1px solid var(--line);font-size:11px;text-align:center}
.cal-row span{display:flex;align-items:center;justify-content:center;border-right:1px solid var(--line)}
.cal-row span:last-child{border-right:0}
.cal-row .off{color:#aaa}
.cal-row .today{background:#1c1c1c;color:#fff}

.testimonials{left:632px;top:713px;width:205px}
.testimonial-video{margin-top:10px;width:205px;height:137px;position:relative;
  background:linear-gradient(135deg,#a6b98a 0%,#d8d2c2 45%,#7a8f6a 100%)}
.testimonials p{font-size:10px;line-height:15.5px;color:var(--muted);margin-top:9px}

/* footer */
.footer{left:0;top:1085px;width:893px;height:115px;background:var(--footer);border-top:1px solid #e6e6e6}
.footer-nav{left:49px;top:1109px;font-size:11.5px;color:#444;display:flex;gap:6px}
.copyright{left:50px;top:1137px;font-size:9px;color:#666}
.social{left:733px;top:1107px;display:flex;gap:3px}
.social span{width:24px;height:24px;border-radius:50%;background:#454545}
</style>
</head>
<body>
<div class="page">
  <header>
    <div class="masthead" role="img" aria-label="Blurred background of blue sky, clouds and a white sand beach"></div>
    <div class="abs brand"><span>Coralwind Stays</span><span class="brand-dot"></span></div>
    <div class="abs search"><span>Search here..</span>
      <svg width="13" height="13" viewBox="0 0 13 13"><circle cx="5.5" cy="5.5" r="4" fill="none" stroke="#888" stroke-width="2"/><line x1="8.5" y1="8.5" x2="12" y2="12" stroke="#888" stroke-width="2"/></svg>
    </div>
    <nav class="abs nav">
      <a href="#">Home</a><a href="#">Palmcrest Holiday Home</a><a href="#">Local Area</a><a href="#">Book Now</a><a href="#">Prices</a><a href="#">Testimonials</a><a href="#">Contact Us</a>
    </nav>
    <div class="abs hero">
      <div class="hero-photo" role="img" aria-label="Holiday villa at dusk with lit swimming pool, terrace and lounger"></div>
      <div class="hero-panel"></div>
    </div>
    <div class="abs hero-copy">
      <h1>Stunning home close to Miami / Enterprise beach!</h1>
      <p>Mauris vel lacus vitae felis vestibulum volutpat. Etiam est nunc, venenatis in, tristique eu, imperdiet ac, nisl.</p>
      <div class="dots"><span></span><span></span><span></span><span></span></div>
    </div>
  </header>

  <section class="abs welcome">
    <h2>Welcome to <b>Coralwind Stays</b></h2>
    <p class="lead">Duis tincidunt lectus quis dui viverra vestibulum. Suspendisse vulputate aliquam dui.</p>
    <p class="body">Nulla elementum dui ut augue. Aliquam vehicula mi at mauris. Maecenas placerat, nisl at consequat rhoncus, sem nunc gravida justo, quis eleifend arcu velit quis lacus. Morbi magna magna, tincidunt a, mattis non, imperdiet vitae, tellus. Sed odio est, auctor ac, sollicitudin in, consequat vitae, orci. Fusce id felis. Vivamus sollicitudin metus eget eros.</p>
  </section>

  <section class="abs properties">
    <h2 class="section-title">Latest Property &amp; Area</h2>
    <div class="prop" style="left:0">
      <div class="thumb" role="img" aria-label="Video: villa pool at sunset" style="background:linear-gradient(180deg,#e7a98a,#6f87a8 55%,#1e5e8c)"><span class="play"><svg width="10" height="12"><polygon points="1,0 10,6 1,12" fill="#fff"/></svg></span></div>
      <h3>Property Name</h3><p>Mauris vel lacus vitae felis vestib</p>
    </div>
    <div class="prop" style="left:185px">
      <div class="thumb" role="img" aria-label="Video: modern house lit at evening" style="background:linear-gradient(180deg,#2c3550,#8a6a4a 55%,#d9a55a)"><span class="play"><svg width="10" height="12"><polygon points="1,0 10,6 1,12" fill="#fff"/></svg></span></div>
      <h3>Property Name</h3><p>Mauris vel lacus vitae felis vestib</p>
    </div>
    <div class="prop" style="left:371px">
      <div class="thumb" role="img" aria-label="Video: beach deck with parasols over turquoise sea" style="background:linear-gradient(180deg,#4fa3dc,#8fd6e4 50%,#2fb6c0 75%,#5a4a3a)"><span class="play"><svg width="10" height="12"><polygon points="1,0 10,6 1,12" fill="#fff"/></svg></span></div>
      <h3>Property Name</h3><p>Mauris vel lacus vitae felis vestib</p>
    </div>
  </section>

  <section class="abs features">
    <h2>House Features</h2>
    <ul>
      <li><svg width="14" height="11"><polyline points="1,6 5,10 13,1" fill="none" stroke="#ee5424" stroke-width="2.5"/></svg>Two luxurious air conditioned bedrooms</li>
      <li><svg width="14" height="11"><polyline points="1,6 5,10 13,1" fill="none" stroke="#ee5424" stroke-width="2.5"/></svg>Sleeps 4 Persons, 3 bathrooms</li>
      <li><svg width="14" height="11"><polyline points="1,6 5,10 13,1" fill="none" stroke="#ee5424" stroke-width="2.5"/></svg>Luxuriously furnished to highest standard</li>
      <li><svg width="14" height="11"><polyline points="1,6 5,10 13,1" fill="none" stroke="#ee5424" stroke-width="2.5"/></svg>Wireless broadband and Personal Computer</li>
      <li><svg width="14" height="11"><polyline points="1,6 5,10 13,1" fill="none" stroke="#ee5424" stroke-width="2.5"/></svg>Playnova games console</li>
      <li><svg width="14" height="11"><polyline points="1,6 5,10 13,1" fill="none" stroke="#ee5424" stroke-width="2.5"/></svg>Private patio overlooking tropical landscape</li>
      <li><svg width="14" height="11"><polyline points="1,6 5,10 13,1" fill="none" stroke="#ee5424" stroke-width="2.5"/></svg>Secure community of only 6 houses</li>
      <li><svg width="14" height="11"><polyline points="1,6 5,10 13,1" fill="none" stroke="#ee5424" stroke-width="2.5"/></svg>2 beaches within 8 minutes walk</li>
    </ul>
  </section>

  <section class="abs attractions">
    <h2>Top 10 Attractions</h2>
    <p>The New Island Privilege Card gives you discount at all of these attractions and is supplied FREE of charge to guests staying in Palmcrest.</p>
    <ul class="attr-list" style="left:6px">
      <li>Miami/Enterprise Beach</li><li>Coastline Safari</li><li>Island Roots and Rhythms</li><li>The Bay Skipper</li><li>DeepBlue Submarines</li>
    </ul>
    <ul class="attr-list" style="left:151px">
      <li>Old Cane Rum Tour</li><li>Bluewake Cruises</li><li>Coral Rock Cave</li><li>Westshore Golf Club</li><li>Merry Buccaneer</li>
    </ul>
  </section>

  <aside class="abs calendar-block">
    <h2 class="sidebar-title">Our Calender</h2>
    <div class="calendar">
      <div class="cal-head"><span>&#9664;</span><span>August 2013</span><span>&#9654;</span></div>
      <div class="cal-days"><span>Su</span><span>Mo</span><span>Tu</span><span>We</span><span>Th</span><span>Fr</span><span>Sa</span></div>
      <div class="cal-row"><span class="off">28</span><span class="off">29</span><span class="off">30</span><span class="off">31</span><span>1</span><span>2</span><span>3</span></div>
      <div class="cal-row"><span>4</span><span>5</span><span>6</span><span>7</span><span>8</span><span>9</span><span>10</span></div>
      <div class="cal-row"><span>11</span><span>12</span><span>13</span><span>14</span><span>15</span><span>16</span><span>17</span></div>
      <div class="cal-row"><span>18</span><span>19</span><span class="today">20</span><span>21</span><span>22</span><span>23</span><span>24</span></div>
      <div class="cal-row"><span>25</span><span>26</span><span>27</span><span>28</span><span>29</span><span>30</span><span class="off">1</span></div>
      <div class="cal-row"><span class="off">2</span><span class="off">3</span><span class="off">4</span><span class="off">5</span><span class="off">6</span><span class="off">7</span><span class="off">8</span></div>
    </div>
  </aside>

  <aside class="abs testimonials">
    <h2 class="sidebar-title">Customer Testimonials</h2>
    <div class="testimonial-video" role="img" aria-label="Video testimonial: family enjoying a barbecue on a garden terrace">
      <span class="play"><svg width="10" height="12"><polygon points="1,0 10,6 1,12" fill="#fff"/></svg></span>
    </div>
    <p>Here are some of the comments guests have made regarding their holiday at Palmcrest.</p>
  </aside>

  <footer>
    <div class="abs footer"></div>
    <div class="abs footer-nav"><span>Home</span>|<span>Palmcrest Holiday Home</span>|<span>Local Area</span>|<span>Book Now</span>|<span>Prices</span>|<span>Testimonials</span>|<span>Contact Us</span></div>
    <div class="abs copyright">Copyright © 2013 Company Name.&nbsp; All right reserved.&nbsp; Term of Use</div>
    <div class="abs social"><span></span><span></span><span></span><span></span></div>
  </footer>
</div>
</body>
</html>
```